Change of trading name, rebrand

existing website to be updated with new theme and logo. existing website is
www.brambleworth.com.au
Industry/Entity Type
Construction
Coding
Coded - Design and coding required
Number of Pages Required
5+ page
Requirements
Must have
- be mobile phone friendly

```html
<!DOCTYPE html>
<html lang="en">
<head>
<meta charset="utf-8">
<meta name="viewport" content="width=device-width, initial-scale=1">
<title>Brambleworth Plant Hire</title>
<link href="https://fonts.googleapis.com/css2?family=Montserrat:wght@400;500;600;700;800&display=swap" rel="stylesheet">
<style>
:root{
  --navy:#272a78;
  --navy-dark:#1d1f5e;
  --ink:#222;
  --muted:#555;
  --grey-bg:#f3f3f3;
  --pill-grey:#8a8a8a;
  --white:#fff;
}
*{box-sizing:border-box;margin:0;padding:0}
html,body{width:1200px;height:5300px;overflow:hidden}
body{font-family:'Montserrat',sans-serif;color:var(--ink);background:var(--white);position:relative}
.abs{position:absolute}
.pill{display:inline-flex;align-items:center;gap:10px;border-radius:40px;font-weight:600;text-transform:uppercase;letter-spacing:.3px;white-space:nowrap}
.pill svg{flex:none}
.btn-navy{background:var(--navy);color:#fff;font-size:12px;height:44px;padding:0 20px 0 28px}
.btn-grey{background:var(--pill-grey);color:#fff;font-size:16px;height:62px;padding:0 26px 0 34px}
/* header */
.site-header{top:0;left:0;width:1200px;height:140px;background:#fff}
.brand{left:76px;top:28px;display:flex;align-items:center;gap:12px;font-weight:800;font-size:24px;color:var(--navy)}
.brand .mark{width:34px;height:34px;background:var(--navy)}
.brand small{display:block;font-size:11px;letter-spacing:4px;color:var(--ink);font-weight:700}
.top-actions{right:72px;top:28px;display:flex;gap:18px}
.phone-pill{background:var(--navy);color:#fff;font-size:13px;height:38px;padding:0 22px 0 8px;text-transform:none}
.phone-pill .ic{width:26px;height:26px;border-radius:50%;background:#fff;display:flex;align-items:center;justify-content:center}
.contact-pill{background:#111;color:#fff;font-size:12px;height:38px;padding:0 30px}
.main-nav{right:72px;top:85px;display:flex;gap:34px;font-size:14px;color:#444;font-weight:500;text-transform:uppercase}
.main-nav .active{color:var(--navy);border-bottom:3px solid var(--navy);padding-bottom:10px}
/* hero */
.hero{top:140px;left:0;width:1200px;height:663px;background:linear-gradient(135deg,#6b6157 0%,#8e7d6b 30%,#c9653a 55%,#7c7064 80%,#5a534d 100%)}
.hero-title{top:210px;width:100%;text-align:center;color:#fff;font-size:50px;font-weight:700}
.hero-sub{top:290px;width:100%;text-align:center;color:#fff;font-size:22px;font-weight:500}
.hero-btn{left:505px;top:350px;background:#fff;color:var(--navy);font-size:14px;height:54px;padding:0 20px 0 32px}
.dots{top:593px;left:0;width:100%;display:flex;justify-content:center;gap:12px;align-items:center}
.dots span{width:11px;height:11px;border-radius:50%;background:#fff}
.dots .on{width:26px;height:6px;border-radius:3px}
/* features */
.features{top:803px;left:0;width:1200px;height:335px;background:linear-gradient(90deg,#2b2d86,#33359a 50%,#2a2c83)}
.feature{top:62px;width:210px;text-align:center;color:#fff;font-size:21px;line-height:31px}
.feature .ring{width:132px;height:132px;border-radius:50%;border:4px solid #fff;margin:0 auto 30px;display:flex;align-items:center;justify-content:center}
.feature .ring div{width:106px;height:106px;border-radius:50%;background:#fff;display:flex;align-items:center;justify-content:center}
/* section heads */
.eyebrow{font-size:21px;font-weight:500;color:var(--ink);display:flex;align-items:center;gap:8px;white-space:nowrap}
.eyebrow .line{display:inline-block;height:2px;background:var(--ink);width:110px;position:relative}
.eyebrow .line::before{content:"";position:absolute;top:-3px;width:8px;height:8px;border-radius:50%;background:var(--ink)}
.eyebrow .line.r::before{left:0}
.eyebrow .line.l::before{right:0}
.h-big{color:var(--navy);font-weight:500;white-space:nowrap}
/* about */
.about-text{left:129px;top:1375px;width:515px;font-size:15px;line-height:30px;color:var(--muted);text-align:justify}
.about-photo{left:700px;top:1255px;width:380px;height:365px;background:#fff;padding:12px;box-shadow:0 4px 16px rgba(0,0,0,.18);border-radius:0 0 50px 0}
.about-photo div{width:100%;height:100%;background:linear-gradient(160deg,#cfd3d8,#8ea3bd 45%,#3f5fa3 70%,#6c7a55);border-radius:0 0 40px 0}
/* plant hire */
.service-img{left:100px;width:460px;height:266px;border-radius:12px;box-shadow:0 4px 12px rgba(0,0,0,.2)}
.service{left:609px;width:490px}
.service h3{font-size:32px;font-weight:600;color:var(--ink)}
.service .bar{width:68px;height:4px;background:var(--navy);margin:14px 0 20px}
.service p{font-size:15px;line-height:30px;color:var(--muted);text-align:justify;margin-bottom:16px}
/* projects */
.projects{top:3108px;left:0;width:1200px;height:1121px;background:var(--grey-bg)}
.card{width:515px;height:286px;background:#fff;border-radius:12px;box-shadow:0 3px 12px rgba(0,0,0,.12);padding:6px;display:flex;gap:20px}
.card .img{width:228px;height:274px;border-radius:10px;flex:none}
.card .body{flex:1;min-width:0}
.card h4{font-size:21px;font-weight:600;color:var(--navy);line-height:31px;margin-top:34px}
.card .client{font-size:17px;font-weight:600;margin:8px 0 14px;white-space:nowrap}
.card .year{font-size:15px;color:var(--ink);white-space:nowrap}
.card .pill{margin-top:30px;height:34px;font-size:10px;padding:0 12px 0 22px}
/* cta */
.cta{top:4229px;left:0;width:1200px;height:439px;background:var(--navy)}
.cta-img{left:0;top:0;width:640px;height:439px;background:linear-gradient(110deg,#b9b09a,#d8b233 40%,#c7a026 60%,rgba(39,42,120,.9) 100%)}
.cta .eyebrow{color:#fff}
.cta .eyebrow .line{background:#fff}
.cta .eyebrow .line::before{background:#fff}
.cta h2{color:#fff;font-size:48px;font-weight:500;line-height:60px;white-space:nowrap}
.cta-btn{background:#fff;color:var(--navy);font-size:15px;height:56px;padding:0 20px 0 26px}
/* partners */
.partners{top:4668px;left:0;width:1200px;height:199px;background:#fff;display:flex;justify-content:center;gap:55px;padding-top:90px}
.partners span{width:80px;height:40px;background:#dcdcdc;border-radius:6px}
/* footer */
.footer{top:4867px;left:0;width:1200px;height:433px;background:var(--navy);color:#fff}
.footer-cap{left:76px;top:0;width:1050px;height:42px;background:#fff;border-radius:0 0 28px 28px}
.slider-nav{left:568px;top:-14px;display:flex;gap:8px}
.slider-nav span{width:28px;height:28px;border-radius:50%;background:var(--navy-dark);display:flex;align-items:center;justify-content:center;border:2px solid #fff}
.foot-brand{left:76px;top:120px;font-size:26px;font-weight:800;display:flex;align-items:center;gap:12px}
.foot-brand .mark{width:36px;height:36px;background:#fff}
.foot-contact{top:160px;display:flex;gap:14px;font-size:12px;line-height:17px}
.foot-contact .ic{width:28px;height:28px;background:#fff;border-radius:5px;display:flex;align-items:center;justify-content:center}
.foot-contact b{font-weight:600;text-transform:uppercase}
.foot-rule{left:76px;top:284px;width:1050px;height:1px;background:rgba(255,255,255,.35)}
.foot-nav{top:312px;left:0;width:100%;display:flex;justify-content:center;gap:36px;font-size:13px;font-weight:500;text-transform:uppercase}
.copyright{top:371px;left:0;width:1200px;height:62px;background:var(--navy-dark);font-size:11px;padding:0 76px;display:flex;align-items:center;justify-content:space-between}
.social{display:flex;gap:8px}
.social span{width:28px;height:28px;border:1px solid #fff;border-radius:4px;display:flex;align-items:center;justify-content:center}
.social span i{width:10px;height:10px;background:#fff;display:block}
</style>
</head>
<body>

<header class="site-header abs">
  <div class="brand abs"><span class="mark"></span><span>BRAMBLEWORTH<small>PLANT HIRE</small></span></div>
  <div class="top-actions abs">
    <span class="pill phone-pill"><span class="ic"><svg width="14" height="14" viewBox="0 0 24 24"><path fill="#272a78" d="M6.6 10.8a15 15 0 006.6 6.6l2.2-2.2a1 1 0 011-.25 11.4 11.4 0 003.6.57 1 1 0 011 1V20a1 1 0 01-1 1A17 17 0 013 4a1 1 0 011-1h3.5a1 1 0 011 1c0 1.25.2 2.45.57 3.57a1 1 0 01-.25 1z"/></svg></span>1300 555 014</span>
    <span class="pill contact-pill">Contact Us</span>
  </div>
  <nav class="main-nav abs"><span class="active">Home</span><span>About Us</span><span>Plant Hire ▾</span><span>Major Project Snapshot</span><span>Policies</span><span>Jobs</span></nav>
</header>

<section class="hero abs" role="img" aria-label="Orange excavator working on a quarry site with gravel stockpiles">
  <h1 class="hero-title abs">Brambleworth Heavy Equipment Hire</h1>
  <p class="hero-sub abs">Committed to superior quality plant hire services.</p>
  <span class="pill hero-btn abs">Learn More <svg width="20" height="20" viewBox="0 0 20 20"><circle cx="10" cy="10" r="10" fill="#272a78"/><path d="M6 10h7M10 7l3 3-3 3" stroke="#fff" stroke-width="2" fill="none"/></svg></span>
  <div class="dots abs"><span class="on"></span><span></span><span></span><span></span></div>
</section>

<section class="features abs">
  <div class="feature abs" style="left:72px"><div class="ring"><div><svg width="50" height="50" viewBox="0 0 50 50"><circle cx="25" cy="20" r="10" fill="#272a78"/><path d="M8 46c0-10 8-16 17-16s17 6 17 16z" fill="#272a78"/></svg></div></div>20+ Years of<br>Experience</div>
  <div class="feature abs" style="left:280px"><div class="ring"><div><svg width="54" height="50" viewBox="0 0 54 50"><rect x="6" y="30" width="30" height="10" fill="#272a78"/><rect x="14" y="20" width="12" height="12" fill="#272a78"/><path d="M26 24l14-14 8 12" stroke="#272a78" stroke-width="4" fill="none"/><rect x="6" y="42" width="30" height="5" rx="2" fill="#272a78"/></svg></div></div>100+ Machines<br>In Fleet</div>
  <div class="feature abs" style="left:490px"><div class="ring"><div><svg width="50" height="50" viewBox="0 0 50 50"><rect x="8" y="26" width="28" height="10" fill="#272a78"/><rect x="14" y="14" width="12" height="12" fill="#272a78"/><rect x="8" y="38" width="34" height="6" rx="3" fill="#272a78"/></svg></div></div>QLD's Largest<br>Suppliers</div>
  <div class="feature abs" style="left:706px"><div class="ring"><div><svg width="50" height="50" viewBox="0 0 50 50"><circle cx="25" cy="18" r="9" fill="#272a78"/><path d="M10 46l4-14h22l4 14z" fill="#272a78"/></svg></div></div>Onsite<br>Servicing</div>
  <div class="feature abs" style="left:916px"><div class="ring"><div><svg width="40" height="50" viewBox="0 0 40 50"><path d="M8 6h24l-4 18H12z" fill="#272a78"/><rect x="16" y="24" width="8" height="20" fill="#272a78"/></svg></div></div>Custom Machine<br>Attachments</div>
</section>

<div class="eyebrow abs" style="left:129px;top:1238px">Who We Are <span class="line r"></span></div>
<h2 class="h-big abs" style="left:129px;top:1265px;font-size:48px">About Brambleworth</h2>
<p class="about-text abs">Brambleworth Resources Pty Ltd trading as Brambleworth Heavy Equipment is a privately owned company that was established in 2010. Our founder saw a need in the market for a plant and equipment supplier who was committed to the successful delivery of client's projects. With this vision and focus Brambleworth has successfully seen our clients deliver on-time and on- budget.</p>
<span class="pill btn-navy abs" style="left:131px;top:1573px">Read More <svg width="18" height="18" viewBox="0 0 20 20"><circle cx="10" cy="10" r="10" fill="#fff"/><path d="M6 10h7M10 7l3 3-3 3" stroke="#272a78" stroke-width="2" fill="none"/></svg></span>
<div class="about-photo abs"><div role="img" aria-label="Company founder standing beside a work vehicle"></div></div>

<div class="eyebrow abs" style="left:0;width:1200px;top:1716px;justify-content:center"><span class="line l" style="width:70px"></span> Who We Do <span class="line r" style="width:70px"></span></div>
<h2 class="h-big abs" style="left:0;width:1200px;top:1745px;font-size:60px;text-align:center">Plant Hire</h2>
<p class="abs" style="left:0;width:1200px;top:1838px;text-align:center;font-size:15px;line-height:30px;color:#333">Reliable Plant Hire Spanning Queensland &amp; Surrounds We Have One of the Largest<br>&amp; Most Versatile Fleets in South East Queensland.</p>

<div class="service-img abs" style="top:1940px;background:linear-gradient(160deg,#9fc3e8,#d8d6cc 45%,#d2612e 65%,#8b8a82)" role="img" aria-label="Orange excavator on a school building site"></div>
<div class="service abs" style="top:1943px"><h3>Excavators &amp; Diggers for Hire</h3><div class="bar"></div><p>We are proud of our broad range of excavators fitted with state-of-the-art GPS, spanning reliable and trusted brands such as Crestline excavators for hire, Koruma excavators for hire,</p><span class="pill btn-navy" style="height:36px;font-size:11px;padding:0 12px 0 20px">Read More <svg width="16" height="16" viewBox="0 0 20 20"><circle cx="10" cy="10" r="10" fill="#fff"/><path d="M6 10h7M10 7l3 3-3 3" stroke="#272a78" stroke-width="2" fill="none"/></svg></span></div>

<div class="service-img abs" style="top:2272px;background:linear-gradient(160deg,#9cc2e6,#cdbb6a 45%,#d9b43a 65%,#7a7463)" role="img" aria-label="Yellow dozer parked in a machinery yard"></div>
<div class="service abs" style="top:2275px"><h3>Dozers for Hire</h3><div class="bar"></div><p>The most prolific brands of dozer manufacturers are Crestline &amp; Koruma – and we have both machine brands available for hire based on your preference – in a range of sizes suitable for bulk earthworks and detailed earthworks.</p><span class="pill btn-navy" style="height:36px;font-size:11px;padding:0 12px 0 20px">Read More <svg width="16" height="16" viewBox="0 0 20 20"><circle cx="10" cy="10" r="10" fill="#fff"/><path d="M6 10h7M10 7l3 3-3 3" stroke="#272a78" stroke-width="2" fill="none"/></svg></span></div>

<div class="service-img abs" style="top:2624px;background:linear-gradient(170deg,#4f8fd8,#9ec5ea 40%,#e0b23a 60%,#b49a55)" role="img" aria-label="Yellow articulated dump truck on a grassy lot"></div>
<div class="service abs" style="top:2627px"><h3>Dump Trucks For Hire</h3><div class="bar"></div><p>Our new and well-maintained fleet of articulated dump trucks for hire ranging from 25 tonne capacity through to 40 tonne. We own and operate a fleet of Belmont and Crestline articulated dump trucks</p><span class="pill btn-navy" style="height:36px;font-size:11px;padding:0 12px 0 20px">Read More <svg width="16" height="16" viewBox="0 0 20 20"><circle cx="10" cy="10" r="10" fill="#fff"/><path d="M6 10h7M10 7l3 3-3 3" stroke="#272a78" stroke-width="2" fill="none"/></svg></span></div>

<span class="pill btn-grey abs" style="left:512px;top:2964px">View All <svg width="24" height="24" viewBox="0 0 20 20"><circle cx="10" cy="10" r="10" fill="#fff"/><path d="M6 10h7M10 7l3 3-3 3" stroke="#8a8a8a" stroke-width="2" fill="none"/></svg></span>

<section class="projects abs">
  <div class="eyebrow abs" style="left:0;width:1200px;top:110px;justify-content:center"><span class="line l" style="width:200px"></span> Brambleworth Projects <span class="line r" style="width:260px"></span></div>
  <h2 class="h-big abs" style="left:0;width:1200px;top:140px;font-size:60px;text-align:center">Major Project Snapshot</h2>
  <p class="abs" style="left:0;width:1200px;top:232px;text-align:center;font-size:16px;color:#333">We're incredibly proud of our major project experience.</p>

  <div class="card abs" style="left:72px;top:312px"><div class="img" style="background:linear-gradient(160deg,#8a8c7a,#c9aa42 50%,#6d6a5c)" role="img" aria-label="Dozer on a road upgrade site"></div><div class="body"><h4>Marlo Enhancement Project (MEP) Brisbane</h4><p class="client">Client – Northline Civil</p><p class="year">Commencement Year – 2017</p><span class="pill btn-navy">Read More <svg width="14" height="14" viewBox="0 0 20 20"><circle cx="10" cy="10" r="10" fill="#fff"/><path d="M6 10h7M10 7l3 3-3 3" stroke="#272a78" stroke-width="2" fill="none"/></svg></span></div></div>
  <div class="card abs" style="left:613px;top:312px"><div class="img" style="background:linear-gradient(170deg,#bcd3ea,#d06640 50%,#6f6d66)" role="img" aria-label="Long reach excavator on a river barge"></div><div class="body"><h4>Riverside Drive Upgrade, Brisbane</h4><p class="client">Client – Harbourview Build</p><p class="year">Commencement Year – 2016</p><span class="pill btn-navy">Read More <svg width="14" height="14" viewBox="0 0 20 20"><circle cx="10" cy="10" r="10" fill="#fff"/><path d="M6 10h7M10 7l3 3-3 3" stroke="#272a78" stroke-width="2" fill="none"/></svg></span></div></div>
  <div class="card abs" style="left:72px;top:623px"><div class="img" style="background:linear-gradient(160deg,#c7c3b8,#d86a35 50%,#a9a59a)" role="img" aria-label="Orange excavator working on a gravel pad"></div><div class="body"><h4>Eastway Upgrade Stage 2, Brisbane</h4><p class="client">Client – Harbourview Build</p><p class="year">Commencement Year – 2016</p><span class="pill btn-navy">Read More <svg width="14" height="14" viewBox="0 0 20 20"><circle cx="10" cy="10" r="10" fill="#fff"/><path d="M6 10h7M10 7l3 3-3 3" stroke="#272a78" stroke-width="2" fill="none"/></svg></span></div></div>
  <div class="card abs" style="left:613px;top:623px"><div class="img" style="background:linear-gradient(170deg,#3f7fd0,#e0b53c 50%,#6a5d4c)" role="img" aria-label="Yellow excavator at a rail works site"></div><div class="body"><h4>Tallowood, QLD<br>Rail</h4><p class="client">Client – Stonegate Civil</p><p class="year">Commencement Year – 2016</p><span class="pill btn-navy">Read More <svg width="14" height="14" viewBox="0 0 20 20"><circle cx="10" cy="10" r="10" fill="#fff"/><path d="M6 10h7M10 7l3 3-3 3" stroke="#272a78" stroke-width="2" fill="none"/></svg></span></div></div>

  <span class="pill btn-grey abs" style="left:512px;top:971px">View All <svg width="24" height="24" viewBox="0 0 20 20"><circle cx="10" cy="10" r="10" fill="#fff"/><path d="M6 10h7M10 7l3 3-3 3" stroke="#8a8a8a" stroke-width="2" fill="none"/></svg></span>
</section>

<section class="cta abs">
  <div class="cta-img abs" role="img" aria-label="Yellow articulated dump truck parked on a site"></div>
  <div class="eyebrow abs" style="left:663px;top:96px">Get In Touch <span class="line r"></span></div>
  <h2 class="abs" style="left:663px;top:128px">Contact Us Today<br>For A FREE QUOTE</h2>
  <span class="pill cta-btn abs" style="left:665px;top:291px">Get A Quote <svg width="20" height="20" viewBox="0 0 20 20"><circle cx="10" cy="10" r="10" fill="#272a78"/><path d="M6 10h7M10 7l3 3-3 3" stroke="#fff" stroke-width="2" fill="none"/></svg></span>
</section>

<section class="partners abs" aria-label="Partners"><span></span><span></span><span></span><span></span><span></span><span></span><span></span></section>

<footer class="footer abs">
  <div class="footer-cap abs"></div>
  <div class="slider-nav abs"><span><svg width="10" height="10" viewBox="0 0 10 10"><path d="M7 1L3 5l4 4" stroke="#fff" stroke-width="2" fill="none"/></svg></span><span><svg width="10" height="10" viewBox="0 0 10 10"><path d="M3 1l4 4-4 4" stroke="#fff" stroke-width="2" fill="none"/></svg></span></div>
  <div class="foot-brand abs"><span class="mark"></span>BRAMBLEWORTH</div>
  <div class="foot-contact abs" style="left:343px"><span class="ic"><svg width="14" height="14" viewBox="0 0 24 24"><path fill="#272a78" d="M6.6 10.8a15 15 0 006.6 6.6l2.2-2.2a1 1 0 011-.25 11.4 11.4 0 003.6.57 1 1 0 011 1V20a1 1 0 01-1 1A17 17 0 013 4a1 1 0 011-1h3.5a1 1 0 011 1c0 1.25.2 2.45.57 3.57a1 1 0 01-.25 1z"/></svg></span><div><b>Call Us</b><br>1300 555 014</div></div>
  <div class="foot-contact abs" style="left:562px"><span class="ic"><svg width="14" height="12" viewBox="0 0 14 12"><rect x="0" y="1" width="14" height="10" fill="#272a78"/><path d="M0 1l7 6 7-6" stroke="#fff" fill="none"/></svg></span><div><b>Email Us</b><br>info@brambleworth.com.au</div></div>
  <div class="foot-contact abs" style="left:848px"><span class="ic"><svg width="12" height="16" viewBox="0 0 12 16"><path d="M6 0a6 6 0 016 6c0 4-6 10-6 10S0 10 0 6a6 6 0 016-6z" fill="#272a78"/><circle cx="6" cy="6" r="2" fill="#fff"/></svg></span><div>48 Saddle Rd,<br>Kestrel QLD 4210</div></div>
  <div class="foot-rule abs"></div>
  <nav class="foot-nav abs"><span>Home</span><span>About Us</span><span>Plant Hire</span><span>Major Project Snapshot</span><span>Policies</span><span>Jobs</span><span>Contact Us</span></nav>
  <div class="copyright abs"><span>Copyright © 2023 All Rights Reserved By Brambleworth Plant Hire</span><div class="social"><span><i></i></span><span><i></i></span><span><i></i></span><span><i></i></span></div></div>
</footer>

</body>
</html>
```